R T Security Flyer - Security Based Company

Security company offering installation of CCTV and Intruder alarm systems mainly but not limited to home alarms. Feel free to be creative

Target Market(s)

Residential and Commercial properties, Facility Managers, local business

Requirements
Must have
• smart professional finish, logo and latest up to date pictures if on kit

```html
<!DOCTYPE html>
<html lang="en">
<head>
<meta charset="utf-8">
<title>R T Security Systems Flyer</title>
<link rel="stylesheet" href="https://fonts.googleapis.com/css2?family=Arimo:wght@400;700&display=swap">
<style>
:root{
  --blue:#2a6d9c;
  --blue-dark:#1d5580;
  --blue-text:#1f5f8b;
  --orange:#ef4e23;
  --white:#ffffff;
  --ink:#222222;
  --photo-wall:#dfe3e6;
}
*{margin:0;padding:0;box-sizing:border-box}
html,body{width:846px;height:1200px;overflow:hidden;background:var(--white)}
body{font-family:"Arimo",Arial,sans-serif;color:var(--ink)}
.flyer{position:relative;width:846px;height:1200px;overflow:hidden;background:var(--white)}

.brand{position:absolute;left:20px;top:118px;width:210px;display:flex;align-items:center;justify-content:center;gap:8px}
.brand-dot{width:14px;height:14px;border-radius:50%;background:var(--orange)}
.brand-name{font-size:22px;font-weight:700;color:var(--orange);line-height:1}

.photo-phone{position:absolute;left:244px;top:0;width:602px;height:236px;
  background:linear-gradient(120deg,#d6d2cc 0%,#9aa3ab 45%,#4d5966 70%,#c8c3bd 100%)}

.hero-band{position:absolute;left:0;top:238px;width:846px;height:178px;
  background:linear-gradient(90deg,var(--blue-dark),var(--blue))}
.hero-question{position:absolute;left:138px;top:287px;width:280px;
  font-size:24px;font-weight:700;line-height:30px;color:var(--white)}

.name-bar{position:absolute;left:0;top:414px;width:552px;height:27px;background:var(--orange);
  color:var(--white);font-size:16px;font-weight:700;text-align:center;line-height:27px;padding-right:60px}

.photo-room{position:absolute;left:530px;top:416px;width:316px;height:610px;
  background:linear-gradient(180deg,var(--photo-wall),#cdd3d8 60%,#e6e8ea)}

.badge{position:absolute;left:506px;top:202px;width:260px;height:260px;border-radius:50%;
  background:var(--white);border:12px solid var(--orange);
  display:flex;flex-direction:column;align-items:center;justify-content:center;text-align:center;font-weight:700}
.badge-lead{font-size:20px;color:var(--blue-text);line-height:1.2}
.badge-life{font-size:76px;color:var(--orange);line-height:1;margin:0 0 2px}
.badge-tail{font-size:20px;color:var(--blue-text);line-height:1.25}
.badge-tail em{font-style:normal;color:var(--orange)}

.photo-keypad{position:absolute;left:526px;top:733px;width:250px;height:284px;background:var(--white);
  padding:10px;box-shadow:0 2px 6px rgba(0,0,0,.25)}
.photo-keypad div{width:100%;height:100%;background:linear-gradient(150deg,#eef0f1,#cfd4d8 55%,#b9a79a)}

.features{position:absolute;left:0;top:440px;width:530px;list-style:none}
.feature{display:flex;align-items:center;padding-left:12px}
.feature:nth-child(1){height:82px}
.feature:nth-child(2){height:83px}
.feature:nth-child(3){height:97px}
.feature:nth-child(4){height:104px}
.feature:nth-child(5){height:105px}
.feature:nth-child(6){height:109px}
.feature svg{flex:0 0 48px;width:48px;height:48px;margin-right:24px}
.feature p{width:432px;font-size:18px;line-height:1.45;color:var(--ink)}

.footer{position:absolute;left:0;top:1026px;width:846px;height:174px;background:var(--blue)}
.footer-cta{position:absolute;left:18px;top:46px;width:210px;font-size:12.5px;font-weight:700;line-height:1.35;color:var(--white)}
.accreditations{position:absolute;left:245px;top:14px;width:356px;height:160px;background:var(--white);
  display:flex;align-items:flex-start;justify-content:space-around;padding-top:12px}
.accreditation{display:flex;flex-direction:column;align-items:center}
.cert-seal{width:92px;height:92px;border-radius:50%;background:var(--blue-dark)}
.cert-caption{margin-top:8px;font-size:14px;font-weight:700;color:var(--blue-dark);text-align:center;line-height:1.25}
.listing-mark{width:130px;height:30px;margin-top:42px;background:var(--orange)}
.contact{position:absolute;left:618px;top:38px;width:220px;text-align:center;color:var(--white);font-size:13.5px;line-height:1.45}
.contact .small{font-size:10.5px}
.contact .gap{margin-top:14px}
</style>
</head>
<body>
<div class="flyer">

  <div class="brand">
    <span class="brand-dot"></span>
    <span class="brand-name">R T Security</span>
  </div>

  <div class="photo-phone" role="img" aria-label="Photo of a hand holding a smartphone showing a smart thermostat app, with a coffee cup behind"></div>

  <div class="hero-band"></div>
  <div class="photo-room" role="img" aria-label="Photo of a wall-mounted smart home control panel"></div>
  <h1 class="hero-question">Are you looking to keep you or your premises safe?</h1>

  <div class="name-bar">RT SECURITY SYSTEMS</div>

  <div class="badge">
    <span class="badge-lead">Connect your</span>
    <span class="badge-life">LIFE</span>
    <span class="badge-tail">to your home<br>and your<br><em>security.</em></span>
  </div>

  <ul class="features">
    <li class="feature">
      <svg viewBox="0 0 48 48" aria-hidden="true"><path fill="#1f5f8b" d="M12 22V10a3 3 0 0 1 6 0v10h1V6a3 3 0 0 1 6 0v14h1V8a3 3 0 0 1 6 0v13h1v-8a3 3 0 0 1 6 0v17c0 9-6 15-14 15h-3c-5 0-8-3-11-7l-6-9a3 3 0 0 1 5-3l2 3z"/></svg>
      <p>We install, maintain and repair all intruder alarms, CCTV, intercom and access control</p>
    </li>
    <li class="feature">
      <svg viewBox="0 0 48 48" aria-hidden="true"><circle cx="24" cy="24" r="20" fill="none" stroke="#1f5f8b" stroke-width="3"/><circle cx="17" cy="19" r="2.5" fill="#1f5f8b"/><circle cx="31" cy="19" r="2.5" fill="#1f5f8b"/><path d="M14 28q10 10 20 0" fill="none" stroke="#1f5f8b" stroke-width="3" stroke-linecap="round"/></svg>
      <p>Feel at ease with monitoring services and police response tailored to suit you and your business</p>
    </li>
    <li class="feature">
      <svg viewBox="0 0 48 48" aria-hidden="true"><rect x="13" y="3" width="22" height="42" rx="3" fill="none" stroke="#1f5f8b" stroke-width="3"/><line x1="20" y1="40" x2="28" y2="40" stroke="#1f5f8b" stroke-width="2.5"/></svg>
      <p>View, control and manage your security systems anywhere in the world with smartphone apps</p>
    </li>
    <li class="feature">
      <svg viewBox="0 0 48 48" aria-hidden="true"><circle cx="24" cy="24" r="21" fill="#1f5f8b"/><path fill="#ffffff" d="M10 14l6 2 3 6-4 4 2 6-4 2-4-8zM26 6l8 3-2 5-5 1-2 5 5 4 8-1 4 6-4 9-6 2 1-7-5-4 1-6-6-3 1-8z"/></svg>
      <p>We can takeover any existing security system and offer maintenance checks to guarantee the best performance for you and your premises</p>
    </li>
    <li class="feature">
      <svg viewBox="0 0 48 48" aria-hidden="true"><polyline points="2,26 12,26 16,18 21,34 27,10 32,30 35,26 46,26" fill="none" stroke="#1f5f8b" stroke-width="3" stroke-linejoin="round" stroke-linecap="round"/></svg>
      <p>We understand that being security conscious is ever increasing, protecting your property and family is a number one priority</p>
    </li>
    <li class="feature">
      <svg viewBox="0 0 48 48" aria-hidden="true"><g fill="#1f5f8b"><circle cx="9" cy="11" r="4"/><circle cx="24" cy="9" r="4.5"/><circle cx="39" cy="11" r="4"/><rect x="4" y="17" width="10" height="16" rx="2"/><rect x="18.5" y="15" width="11" height="18" rx="2"/><rect x="34" y="17" width="10" height="16" rx="2"/><rect x="5" y="32" width="3.5" height="12"/><rect x="9.5" y="32" width="3.5" height="12"/><rect x="20" y="32" width="3.5" height="13"/><rect x="24.5" y="32" width="3.5" height="13"/><rect x="35" y="32" width="3.5" height="12"/><rect x="39.5" y="32" width="3.5" height="12"/></g></svg>
      <p>Our fully insured and accredited team offer quality, safety and cost efficiency throughout and whole process</p>
    </li>
  </ul>

  <div class="photo-keypad" role="img" aria-label="Photo of a finger pressing a button on a white intruder alarm keypad"><div></div></div>

  <footer class="footer">
    <p class="footer-cta">If you are looking to improve the security in your home, office or commercial property then call a member of our team today for a free quote.</p>
    <div class="accreditations">
      <div class="accreditation">
        <div class="cert-seal"></div>
        <div class="cert-caption">Intruder Alarm<br>Systems</div>
      </div>
      <div class="accreditation">
        <div class="listing-mark"></div>
      </div>
    </div>
    <div class="contact">
      <div>01632 960418,</div>
      <div class="small">operations@rtsecuritysystems.co.uk,</div>
      <div>www.rtsecuritysystems.co.uk,</div>
      <div class="gap">14 Harrow Lane, Millbridge,<br>Essex, CM99 2QT</div>
    </div>
  </footer>

</div>
</body>
</html>
```